Employee I.D. Card - Badge

We need an employee I.D. card designed. Our employees are going to be wearing these. I would like to have it look nice. Something professional yet cool (not uptight if that makes sense).
Project Scope:
Vertical orientation
Company name ------------- (Bright and Tidy)
Website ------------- (brightandtidymn.example)
Employee Picture
background check image
front and back designed - same design on either side
You can create the card without having the employee images on them.
Here are the dimensions -
2.125 x 3.370 inches
Double sided - same design can be used front and back
Background badge - I would like to add an image that shows that the employee has taken a background check. I've added the press-kit for the company we use. If you have a better idea than incorporating their logo, we can certainly do something different.
Example image-
https://www.findwell-search.example/results?q=background+check+badge&mode=images
The print company will set up the names.
Logo is attached
Also attached are our business cards. You can use this for an idea of brand/company style.
Our website - brightandtidymn.example

```html
<!DOCTYPE html>
<html lang="en">
<head>
<meta charset="utf-8">
<title>Bright and Tidy – Employee ID Badge</title>
<link rel="stylesheet" href="https://fonts.googleapis.com/css2?family=Bebas+Neue&family=Nunito:wght@800&display=swap">
<style>
  :root {
    --sky-top: #2aa6ec;
    --sky-bottom: #5cc4f3;
    --sky-dot: #4cb5ef;
    --lime: #b8f000;
    --ink: #2b2b2b;
    --white: #ffffff;
    --brand-blue: #2a9fe0;
    --bar-start: #2b7fe0;
    --bar-end: #3fe0f8;
    --watermark: #e6f6fc;
  }
  html, body {
    margin: 0;
    padding: 0;
    overflow: hidden;
    background: var(--white);
  }
  .badge {
    position: relative;
    width: 757px;
    height: 1200px;
    overflow: hidden;
    background: var(--white);
  }
  .badge__art {
    position: absolute;
    inset: 0;
    width: 757px;
    height: 1200px;
  }
  .brand-name {
    position: absolute;
    top: 40px;
    right: 40px;
    width: 250px;
    margin: 0;
    font-family: "Nunito", sans-serif;
    font-weight: 800;
    font-size: 46px;
    line-height: 1;
    color: var(--brand-blue);
    text-align: center;
    text-transform: lowercase;
  }
  .employee-photo {
    position: absolute;
    left: 24px;
    top: 303px;
    width: 420px;
    height: 445px;
    border-radius: 210px 210px 0 0;
    background: linear-gradient(180deg, #e7c3ad 0%, #dcebf7 45%, #c9def0 100%);
  }
  .employee-name {
    position: absolute;
    left: 470px;
    top: 512px;
    width: 240px;
    margin: 0;
    font-family: "Bebas Neue", sans-serif;
    font-weight: 400;
    font-size: 56px;
    line-height: 0.98;
    color: var(--white);
    text-align: center;
  }
  .employee-role {
    position: absolute;
    left: 470px;
    top: 686px;
    width: 260px;
    margin: 0;
    font-family: "Bebas Neue", sans-serif;
    font-weight: 400;
    font-size: 46px;
    line-height: 1;
    color: var(--ink);
    text-align: center;
  }
  .brand-watermark {
    position: absolute;
    left: 230px;
    top: 830px;
    margin: 0;
    font-family: "Nunito", sans-serif;
    font-weight: 800;
    font-size: 120px;
    line-height: 1;
    color: var(--watermark);
    text-transform: lowercase;
    white-space: nowrap;
  }
  .website {
    position: absolute;
    left: 208px;
    top: 1088px;
    margin: 0;
    font-family: "Nunito", sans-serif;
    font-weight: 800;
    font-size: 33px;
    line-height: 40px;
    color: var(--white);
  }
</style>
</head>
<body>
  <main class="badge">
    <svg class="badge__art" viewBox="0 0 757 1200" aria-hidden="true">
      <defs>
        <linearGradient id="sky" x1="0" y1="0" x2="0" y2="1">
          <stop offset="0" stop-color="var(--sky-top)"/>
          <stop offset="1" stop-color="var(--sky-bottom)"/>
        </linearGradient>
        <linearGradient id="bar" x1="0" y1="0" x2="1" y2="0">
          <stop offset="0" stop-color="var(--bar-start)"/>
          <stop offset="1" stop-color="var(--bar-end)"/>
        </linearGradient>
        <linearGradient id="globe" x1="0" y1="0" x2="1" y2="1">
          <stop offset="0" stop-color="#3fd0f5"/>
          <stop offset="1" stop-color="#2a6fe0"/>
        </linearGradient>
      </defs>

      <!-- sky panel -->
      <rect class="sky" x="0" y="0" width="757" height="790" fill="url(#sky)"/>

      <!-- top-right white wave holding the brand name -->
      <path class="brand-wave" d="M410 0 C 430 60, 480 110, 560 150 C 640 185, 700 175, 757 200 L757 0 Z" fill="var(--white)"/>

      <!-- white arc behind the portrait -->
      <path class="portrait-arc" d="M0 548 C 80 470, 250 455, 360 510 C 430 545, 450 600, 450 662 L0 662 Z" fill="var(--white)"/>

      <!-- bubbles -->
      <g class="bubbles" fill="var(--white)">
        <circle cx="78" cy="455" r="9"/>
        <circle cx="95" cy="447" r="5"/>
        <circle cx="95" cy="464" r="4"/>
        <circle cx="440" cy="558" r="9"/>
        <circle cx="426" cy="567" r="5"/>
        <circle cx="442" cy="574" r="4"/>
      </g>

      <!-- lime band and lower white panel -->
      <path class="lime-band" d="M0 662 L757 662 L757 783 L0 706 Z" fill="var(--lime)"/>
      <path class="lower-panel" d="M0 706 L757 783 L757 1200 L0 1200 Z" fill="var(--white)"/>

      <!-- website bar -->
      <rect class="web-bar" x="0" y="1080" width="757" height="56" fill="url(#bar)"/>
    </svg>

    <p class="brand-name">Bright and Tidy</p>

    <div class="employee-photo" role="img" aria-label="Employee portrait photo area"></div>

    <svg class="badge__art" viewBox="0 0 757 1200" aria-hidden="true">
      <!-- background check seal -->
      <g class="check-seal">
        <circle cx="380" cy="469" r="60" fill="var(--lime)"/>
        <circle cx="380" cy="469" r="46" fill="var(--white)"/>
        <circle cx="380" cy="469" r="24" fill="var(--lime)"/>
      </g>
      <!-- globe icon -->
      <g class="globe-icon">
        <circle cx="101" cy="1121" r="53" fill="var(--white)"/>
        <g fill="none" stroke="url(#globe)" stroke-width="4">
          <circle cx="101" cy="1121" r="32"/>
          <ellipse cx="101" cy="1121" rx="14" ry="32"/>
          <line x1="101" y1="1089" x2="101" y2="1153"/>
          <line x1="69" y1="1121" x2="133" y2="1121"/>
          <path d="M74 1104 H128 M74 1138 H128"/>
        </g>
      </g>
    </svg>

    <h1 class="employee-name">Employee<br>Name</h1>
    <p class="employee-role">Ocupation</p>

    <p class="brand-watermark">bright</p>

    <p class="website">brightandtidymn.example</p>
  </main>
</body>
</html>
```